Business Card Design

Need business card design for all carpentry & construction solutions. We would like to see designs that use black as a background with orange writing as it would stand out.

Business

RVK CONTRACTING
MARTIN COLLIER
14 KESTWICK ST
WONGAN HILLS
WA 6603
0487315962
rvkcontracting@mailvesta.com

```html
<!DOCTYPE html>
<html lang="en">
<head>
<meta charset="utf-8">
<title>RVK Contracting – Business Card</title>
<link rel="stylesheet" href="https://fonts.googleapis.com/css2?family=Jost:wght@400&family=Roboto+Condensed:wght@400;700&display=swap">
<style>
  :root {
    --backdrop: #d3d3d3;
    --card: #262728;
    --gold: #d6ab3c;
    --gold-soft: #c99f37;
  }
  * { margin: 0; padding: 0; box-sizing: border-box; }
  html, body {
    width: 1200px;
    height: 781px;
    overflow: hidden;
    background: var(--backdrop);
  }
  .sheet {
    position: relative;
    width: 1200px;
    height: 781px;
  }
  .card {
    position: absolute;
    left: 358px;
    width: 453px;
    height: 251px;
    background: var(--card);
  }
  .card--front { top: 103px; }
  .card--back  { top: 408px; }

  .wordmark {
    position: absolute;
    font-family: "Jost", sans-serif;
    font-weight: 400;
    font-size: 21px;
    letter-spacing: 0.06em;
    color: var(--gold);
    white-space: nowrap;
    line-height: 1;
  }
  .card--front .wordmark {
    right: 40px;
    top: 64px;
  }
  .card--back .wordmark {
    left: 50%;
    top: 50%;
    transform: translate(-50%, -50%);
  }

  .contact {
    position: absolute;
    left: 40px;
    top: 171px;
    font-family: "Roboto Condensed", sans-serif;
    color: var(--gold-soft);
  }
  .contact__name {
    font-weight: 700;
    font-size: 16px;
    color: var(--gold);
    letter-spacing: 0.01em;
    margin-bottom: 9px;
    line-height: 1;
  }
  .contact__line {
    font-weight: 400;
    font-size: 10px;
    line-height: 13.5px;
    white-space: nowrap;
  }
  .contact__label { font-weight: 700; }
</style>
</head>
<body>
  <main class="sheet">
    <section class="card card--front" aria-label="Business card front">
      <div class="wordmark">RVK CONTRACTING</div>
      <div class="contact">
        <p class="contact__name">MARTIN COLLIER</p>
        <p class="contact__line">14 Kestwick Street, Carrow Hills WA 6512</p>
        <p class="contact__line"><span class="contact__label">T:</span> 0487315962 · <span class="contact__label">E:</span> rvkcontracting@mailvesta.com</p>
      </div>
    </section>
    <section class="card card--back" aria-label="Business card back">
      <div class="wordmark">RVK CONTRACTING</div>
    </section>
  </main>
</body>
</html>
```